quorvaAgency Business Card Design Project

We need a business card design for quorvaAgency. quorvaAgency is an underwriting agency. Underwriting agencies act on behalf of insurers, to underwrite insurance. We will be operating in specialised classes of insurance initially and looking to expand from there. We would like to see designs that incorporate our logo colours as well as a contrasting stand out colour - also we'd like the logo itself to be embossed on the card.

Industry/Entity Type

Insurance

Requirements
Must have
• Logo on front
Nice to have
• Logo solely featured on back of card
Should not have
• Please do not use comic cans font :)

```html
<!DOCTYPE html>
<html lang="en">
<head>
<meta charset="utf-8">
<title>quorvaAgency Business Card</title>
<link rel="stylesheet" href="https://fonts.googleapis.com/css2?family=Open+Sans:wght@400;600;700&display=swap">
<style>
  :root {
    --bg: #dcdddf;
    --bg-light: #f1f2f3;
    --navy-deep: #14264a;
    --navy: #0d3a78;
    --brand-blue: #1a5aa8;
    --card-white: #fdfbfc;
    --text-grey: #4a4a4c;
    --silver-dark: #6b6b6e;
    --silver-light: #e4e4e6;
  }
  * { margin: 0; padding: 0; box-sizing: border-box; }
  html, body { width: 1200px; height: 900px; overflow: hidden; }
  body {
    position: relative;
    background: radial-gradient(ellipse at 50% 48%, var(--bg-light) 0%, var(--bg) 70%);
    font-family: "Open Sans", Arial, sans-serif;
  }
  .card { position: absolute; width: 540px; height: 336px; }
  .card svg { position: absolute; inset: 0; }
  .card--front { left: 40px; top: 280px; }
  .card--back { left: 620px; top: 280px; }

  .brand-mark {
    position: absolute;
    border-radius: 50%;
  }
  .card--front .brand-mark {
    width: 110px; height: 110px; left: 208px; top: 68px;
    border: 8px solid var(--card-white);
  }
  .card--back .brand-mark {
    width: 64px; height: 64px; left: 384px; top: 24px;
    border: 5px solid var(--brand-blue);
  }
  .brand-name {
    position: absolute;
    font-weight: 700;
    letter-spacing: -1px;
    white-space: nowrap;
  }
  .card--front .brand-name {
    left: 0; width: 540px; top: 188px; text-align: center;
    font-size: 50px; color: var(--card-white);
  }
  .card--back .brand-name {
    right: 32px; top: 92px;
    font-size: 32px; color: var(--brand-blue);
  }

  .person {
    position: absolute; right: 288px; top: 216px; text-align: right;
  }
  .person__name { font-size: 22px; font-weight: 700; color: var(--brand-blue); line-height: 1.1; }
  .person__role { font-size: 15px; color: var(--text-grey); }
  .divider {
    position: absolute; left: 274px; top: 212px; width: 1px; height: 80px;
    background: var(--silver-dark);
  }
  .contacts {
    position: absolute; left: 286px; top: 218px; list-style: none;
    font-size: 15px; color: var(--text-grey); line-height: 21px;
  }
  .contacts li { display: flex; align-items: center; gap: 10px; }
  .contacts svg { position: static; width: 14px; height: 14px; fill: var(--navy); flex: none; }
</style>
</head>
<body>

<section class="card card--front" aria-label="Card front">
  <svg viewBox="0 0 540 336" width="540" height="336">
    <defs>
      <clipPath id="front-shape"><rect width="540" height="336" rx="16"/></clipPath>
      <radialGradient id="front-navy" cx="50%" cy="35%" r="60%">
        <stop offset="0" stop-color="var(--navy)"/>
        <stop offset="1" stop-color="var(--navy-deep)"/>
      </radialGradient>
      <linearGradient id="front-silver" x1="0" x2="1">
        <stop offset="0" stop-color="var(--silver-dark)"/>
        <stop offset="0.5" stop-color="var(--silver-light)"/>
        <stop offset="1" stop-color="var(--silver-dark)"/>
      </linearGradient>
    </defs>
    <g clip-path="url(#front-shape)">
      <rect width="540" height="336" fill="var(--card-white)"/>
      <path d="M0 0 H540 V232 Q270 372 0 232 Z" fill="url(#front-navy)"/>
      <path d="M0 238 Q270 378 540 238" fill="none" stroke="url(#front-silver)" stroke-width="6"/>
    </g>
  </svg>
  <div class="brand-mark" aria-hidden="true"></div>
  <div class="brand-name">quorvaAgency</div>
</section>

<section class="card card--back" aria-label="Card back">
  <svg viewBox="0 0 540 336" width="540" height="336">
    <defs>
      <clipPath id="back-shape"><rect width="540" height="336" rx="16"/></clipPath>
      <radialGradient id="back-navy" cx="20%" cy="45%" r="70%">
        <stop offset="0" stop-color="var(--navy)"/>
        <stop offset="1" stop-color="var(--navy-deep)"/>
      </radialGradient>
      <linearGradient id="back-silver" x1="0" y1="0" x2="0" y2="1">
        <stop offset="0" stop-color="var(--silver-dark)"/>
        <stop offset="0.45" stop-color="var(--silver-light)"/>
        <stop offset="1" stop-color="var(--silver-dark)"/>
      </linearGradient>
    </defs>
    <g clip-path="url(#back-shape)">
      <rect width="540" height="336" fill="var(--card-white)"/>
      <path d="M0 0 H186 Q50 150 4 336 H0 Z" fill="url(#back-navy)"/>
      <path d="M190 0 Q54 150 8 336" fill="none" stroke="url(#back-silver)" stroke-width="6"/>
      <path d="M540 230 Q505 295 466 336 H540 Z" fill="url(#back-navy)"/>
      <path d="M540 236 Q503 298 462 336" fill="none" stroke="url(#back-silver)" stroke-width="5"/>
    </g>
  </svg>
  <div class="brand-mark" aria-hidden="true"></div>
  <div class="brand-name">quorvaAgency</div>

  <div class="person">
    <div class="person__name">Your Name</div>
    <div class="person__role">consultant</div>
  </div>
  <div class="divider"></div>
  <ul class="contacts">
    <li>
      <svg viewBox="0 0 16 16" aria-hidden="true"><path d="M1 6 Q8 0 15 6 L12 8 L11 6 Q8 5 5 6 L4 8 Z M4 9 H12 L13 14 H3 Z"/></svg>
      +65 20 88 654321
    </li>
    <li>
      <svg viewBox="0 0 16 16" aria-hidden="true"><path d="M1 3 H15 V13 H1 Z M2 4 L8 9 L14 4" stroke="#fff" stroke-width="1"/></svg>
      yourname@quorvaagency.com
    </li>
    <li>
      <svg viewBox="0 0 16 16" aria-hidden="true"><circle cx="8" cy="8" r="7"/><path d="M1 8 H15 M8 1 V15 M8 1 Q3 8 8 15 M8 1 Q13 8 8 15" stroke="#fff" stroke-width="1" fill="none"/></svg>
      www.quorvaagency.com
    </li>
  </ul>
</section>

</body>
</html>
```